Delcourt Realty Business Cards

Design business card

Target Market(s)

High-End Buyer of Real Estate over $1 million dollars

Industry/Entity Type

Realtor

Contact Information for Business Card

Lena Delcourt R(S) LIC.# 41972
Cell 555 246-1938
Email Lena@Delcourt.example
Website IsleFreshHomes.example

Also Need Cards for:

Hank Delcourt R(B) LIC# 69418
C 555 613-7052
E Hank@Delcourt.example
W IsleFreshHomes.example

Colors

Designer to choose colors to be used in the design.

Requirements
Must have
• Address on back:
• 287 Pohaku Cir. , Wailea HI 96753
• Logo on back
Nice to have
• I would like the phone numbers and email address to be big so people can read it easily
Should not have
• Very small print Except For: address (287 Pohaku Cir. Wailea HI 96753)

```html
<!DOCTYPE html>
<html lang="en">
<head>
<meta charset="utf-8">
<title>Delcourt Realty Business Cards</title>
<link href="https://fonts.googleapis.com/css2?family=Newsreader:opsz,wght@6..72,300&display=swap" rel="stylesheet">
<style>
  :root {
    --page: #f1f1f1;
    --card-top: #586c82;
    --card-bottom: #435369;
    --rule: #1d3855;
    --ink: #e4ded2;
  }
  * { margin: 0; padding: 0; box-sizing: border-box; }
  html, body { width: 1200px; height: 900px; overflow: hidden; background: var(--page); }
  .canvas { position: relative; width: 1200px; height: 900px; }
  .card {
    position: absolute;
    top: 340px;
    width: 392px;
    height: 224px;
    background: linear-gradient(180deg, var(--card-top), var(--card-bottom));
    font-family: "Newsreader", Georgia, serif;
    font-weight: 300;
    color: var(--ink);
    overflow: hidden;
  }
  .card--front { left: 169px; }
  .card--back { left: 638px; }
  .id-frame {
    position: absolute; left: 0; top: 0;
    width: 200px; height: 102px;
    border-right: 2px solid var(--rule);
    border-bottom: 2px solid var(--rule);
  }
  .address-frame {
    position: absolute; left: 192px; top: 122px;
    right: 0; bottom: 0;
    border-left: 2px solid var(--rule);
    border-top: 2px solid var(--rule);
  }
  .agent-id {
    position: absolute; left: 35px; top: 30px;
    font-size: 16px; line-height: 18px;
  }
  .contact-list {
    position: absolute; left: 35px; top: 120px;
    list-style: none;
    font-size: 16px; line-height: 25px;
  }
  .address {
    position: absolute; left: 213px; top: 140px;
    font-size: 14px; line-height: 16px;
  }
  .brand-name {
    position: absolute; top: 47px;
    width: 96px; height: 130px;
    display: flex; align-items: center; justify-content: center;
    text-align: center;
    font-size: 19px; line-height: 24px;
    letter-spacing: 0.04em;
  }
  .card--front .brand-name { left: 223px; }
  .card--back .brand-name { left: 42px; }
</style>
</head>
<body>
<div class="canvas">
  <section class="card card--front" aria-label="Business card front">
    <div class="id-frame"></div>
    <p class="agent-id">Lena Delcourt R(S)<br>LIC.# 41972</p>
    <ul class="contact-list">
      <li>555 246-1938</li>
      <li>Lena@Delcourt.example</li>
      <li>IsleFreshHomes.example</li>
    </ul>
    <p class="brand-name">Delcourt<br>Realty</p>
  </section>

  <section class="card card--back" aria-label="Business card back">
    <p class="brand-name">Delcourt<br>Realty</p>
    <div class="address-frame"></div>
    <p class="address">287 Pohaku Cir. , Wailea HI<br>96753</p>
  </section>
</div>
</body>
</html>
```